German Headhunter/ HR Consultancy needs Business Cards Design

We need a business Card Design for our Company in Stuttgart. We are specialized as Headhunter/ HR Consultancy in Placement of specialist and managers in permanent employment. Please refer to our business logo.

```html
<!DOCTYPE html>
<html lang="de">
<head>
<meta charset="utf-8">
<title>Meridian Personalberatung – Visitenkarte</title>
<link rel="stylesheet" href="https://fonts.googleapis.com/css2?family=Montserrat:wght@500;600;700&family=Arimo:wght@400&display=swap">
<style>
  :root {
    --stage: #262626;
    --brand-blue: #3a55a8;
    --brand-grey: #8c8c8c;
    --paper: #ffffff;
    --ink: #1c1c1c;
    --rule: #c9c9c9;
  }
  * { margin: 0; padding: 0; box-sizing: border-box; }
  html, body { width: 1200px; height: 1015px; overflow: hidden; background: var(--stage); }
  .canvas { position: relative; width: 1200px; height: 1015px; }

  .card {
    position: absolute;
    width: 630px;
    height: 360px;
    box-shadow: 0 18px 40px rgba(0,0,0,.55);
  }
  .card--front { left: 70px; top: 80px; background: var(--brand-blue); }
  .card--back  { left: 500px; top: 560px; background: var(--paper); }

  .wordmark { position: absolute; display: flex; align-items: center; gap: 14px; }
  .wordmark__square { width: 34px; height: 34px; }
  .wordmark__name {
    font-family: "Montserrat", sans-serif;
    font-weight: 700;
    font-size: 34px;
    letter-spacing: 2px;
    line-height: 1;
  }
  .wordmark__sub {
    font-family: "Montserrat", sans-serif;
    font-weight: 700;
    font-size: 14.5px;
    letter-spacing: 1.6px;
    line-height: 1;
    margin-top: 4px;
  }
  .card--front .wordmark { left: 48px; bottom: 52px; }
  .card--front .wordmark__square { background: var(--paper); }
  .card--front .wordmark__name,
  .card--front .wordmark__sub { color: var(--paper); }

  .card--back .wordmark { right: 40px; top: 42px; }
  .card--back .wordmark__square { background: var(--brand-blue); }
  .card--back .wordmark__name { color: var(--brand-blue); }
  .card--back .wordmark__sub { color: var(--brand-grey); }

  .divider { position: absolute; left: 40px; right: 40px; top: 150px; height: 1px; background: var(--rule); }

  .person { position: absolute; left: 40px; top: 178px; }
  .person__name {
    font-family: "Montserrat", sans-serif;
    font-weight: 700;
    font-size: 24px;
    letter-spacing: 1px;
    color: var(--brand-blue);
  }
  .person__role {
    font-family: "Arimo", sans-serif;
    font-size: 17px;
    color: var(--ink);
    margin-top: 2px;
    padding-bottom: 10px;
    border-bottom: 1px solid var(--rule);
    width: 230px;
  }
  .contacts { list-style: none; margin-top: 10px; }
  .contacts li {
    display: flex; align-items: center; gap: 10px;
    font-family: "Arimo", sans-serif;
    font-size: 17px;
    color: var(--ink);
    line-height: 26px;
  }
  .contacts svg { width: 18px; height: 18px; fill: none; stroke: var(--brand-blue); stroke-width: 2; }
  .contacts .accent { color: var(--brand-blue); }

  .address {
    position: absolute; right: 40px; top: 236px;
    font-family: "Arimo", sans-serif;
    font-size: 17px; line-height: 24px;
    text-align: right; color: var(--ink);
  }
</style>
</head>
<body>
<main class="canvas">
  <section class="card card--front" aria-label="Vorderseite">
    <div class="wordmark">
      <span class="wordmark__square"></span>
      <div>
        <div class="wordmark__name">MERIDIAN</div>
        <div class="wordmark__sub">PERSONALBERATUNG</div>
      </div>
    </div>
  </section>

  <section class="card card--back" aria-label="Rückseite">
    <div class="wordmark">
      <span class="wordmark__square"></span>
      <div>
        <div class="wordmark__name">MERIDIAN</div>
        <div class="wordmark__sub">PERSONALBERATUNG</div>
      </div>
    </div>

    <div class="divider"></div>

    <div class="person">
      <div class="person__name">LUKAS BERGER</div>
      <div class="person__role">Managing Director</div>
      <ul class="contacts">
        <li>
          <svg viewBox="0 0 24 24" aria-hidden="true"><path d="M5 3h4l2 5-3 2a12 12 0 0 0 6 6l2-3 5 2v4a2 2 0 0 1-2 2A17 17 0 0 1 3 5a2 2 0 0 1 2-2z"/></svg>
          044-555 010 200
        </li>
        <li>
          <svg viewBox="0 0 24 24" aria-hidden="true"><rect x="3" y="5" width="18" height="14"/><path d="M3 5l9 8 9-8"/></svg>
          info@kontaktname.com
        </li>
        <li>
          <svg viewBox="0 0 24 24" aria-hidden="true"><circle cx="12" cy="12" r="9"/><path d="M3 12h18M12 3c3 3 3 15 0 18M12 3c-3 3-3 15 0 18"/></svg>
          <span>www.<span class="accent">firmenname</span>.com</span>
        </li>
      </ul>
    </div>

    <address class="address" style="font-style:normal">
      421, Address line goes here<br>
      45452, Country Name
    </address>
  </section>
</main>
</body>
</html>
```